Consultant Word Template Design

I want to use a word template to submit service proposals to clients. You can visit my web site: Brightwayadvisory.com for content/ design ideas and I am also attaching my flyer. The color scheme should be consistent with my logo, web, flyer, etc. blue and white. I want some core pages: front & back page design, about us, services

Industry/Entity Type

Health Care

Colors

Designer to choose colors to be used in the design.

```html
<!DOCTYPE html>
<html lang="en">
<head>
<meta charset="utf-8">
<title>Brightway Advisory – Proposal Template Pages</title>
<link href="https://fonts.googleapis.com/css2?family=Poppins:wght@400;500;600&family=Open+Sans:ital,wght@0,400;0,600;1,400&display=swap" rel="stylesheet">
<style>
:root{
  --backdrop:#000;
  --paper:#fff;
  --brand:#0a4da2;
  --brand-light:#6fb9ff;
  --brand-mid:#3a8fe0;
  --rule:#a9c6ea;
  --ink:#3d3d3d;
  --ink-dark:#222;
  --grey:#666;
  --grey-band:#d9d9d9;
  --photo-a:#c9ccd0;
  --photo-b:#eef0f2;
}
*{box-sizing:border-box;margin:0;padding:0}
html,body{width:874px;height:1200px;overflow:hidden;background:var(--backdrop)}
.canvas{position:relative;width:874px;height:1200px;background:var(--backdrop)}
.page{position:absolute;width:401px;height:570px;background:var(--paper);overflow:hidden}
.page--cover{left:24px;top:20px}
.page--text{left:450px;top:20px}
.page--tables{left:24px;top:612px}
.page--charts{left:450px;top:612px}
.page-title{position:absolute;left:17px;top:17px;font:600 10.5px/1 "Poppins",sans-serif;color:var(--ink-dark)}
.page--cover .page-title{font-size:13px;top:18px}
.brand{position:absolute;right:14px;top:14px;display:flex;align-items:center;gap:4px;font:600 8.5px/1 "Poppins",sans-serif;color:var(--brand)}
.brand-mark{width:8px;height:8px;background:var(--brand)}
.heading{position:absolute;left:17px;font:600 10px/1 "Poppins",sans-serif;color:var(--brand)}
.body{position:absolute;left:19px;right:17px;font:400 7.2px/12.7px "Open Sans",sans-serif;color:var(--ink);overflow:hidden}
.body p+p{margin-top:12.7px}
.body--quote{font-style:italic;color:var(--brand)}
.cols{position:absolute;left:19px;right:17px;display:grid;grid-template-columns:1fr 1fr;column-gap:16px;font:400 7.2px/12.7px "Open Sans",sans-serif;color:var(--ink);overflow:hidden}
.cols p+p{margin-top:12.7px}
.footer-rule{position:absolute;left:9px;right:9px;top:544px;border-top:1px solid var(--rule)}
.folio{position:absolute;left:0;right:0;top:553px;text-align:center;font:400 7px/1 "Open Sans",sans-serif;color:var(--brand)}
.hero{position:absolute;left:0;top:44px;width:401px;height:152px}
.banner{position:absolute;left:0;top:192px;width:401px;height:44px;background:var(--brand);padding:9px 17px;color:#fff}
.banner-title{font:600 11px/1.2 "Poppins",sans-serif}
.banner-sub{font:600 6.8px/1.4 "Poppins",sans-serif}
.banner-notch{position:absolute;left:24px;top:236px;width:0;height:0;border-left:10px solid transparent;border-right:10px solid transparent;border-top:10px solid var(--brand)}
.table-label{position:absolute;left:17px;font:600 10px/1 "Poppins",sans-serif;color:var(--brand)}
.table-label--muted{color:var(--grey)}
.table{position:absolute;left:18px;width:362px;font:400 7.2px/1 "Open Sans",sans-serif;color:var(--ink)}
.row{display:grid;grid-template-columns:102px 50px 52px 48px 64px 1fr;align-items:center;padding-left:6px}
.row span:not(:first-child){padding-left:4px}
.row--head{height:19px;font-weight:600;color:var(--ink-dark);font-size:6.8px}
.row--body{height:15.2px}
.table--lined .row--head{border-top:1px solid #bbb;border-bottom:1px solid var(--brand)}
.table--lined{border-bottom:2px solid var(--rule)}
.table--lined .row--head+.row--body{margin-top:3px}
.table--shaded .row--head{background:var(--grey-band)}
.table--shaded .row--head+.row--body{margin-top:4px}
.table--shaded{border-bottom:2px solid #eee}
.table--boxed{border:1px solid var(--rule)}
.table--boxed .row{padding-left:12px}
.table--boxed .row--head{background:var(--brand);color:#fff}
.table--boxed .row--head+.row--body{margin-top:5px}
.table--boxed .row--body:last-child{margin-bottom:5px}
.chart{position:absolute;left:0;top:0;width:401px;height:570px}
</style>
</head>
<body>
<main class="canvas">

  <!-- Cover page -->
  <section class="page page--cover">
    <h1 class="page-title">Business Title here</h1>
    <div class="brand"><span class="brand-mark"></span>Brightway Advisory</div>
    <svg class="hero" viewBox="0 0 401 152" role="img" aria-label="Photo of a healthcare team meeting around a table in a bright office">
      <defs>
        <linearGradient id="heroTone" x1="0" y1="0" x2="1" y2="1">
          <stop offset="0" stop-color="var(--photo-a)"/>
          <stop offset="1" stop-color="var(--photo-b)"/>
        </linearGradient>
      </defs>
      <path d="M0 16 Q200 -8 401 16 V152 H0Z" fill="url(#heroTone)"/>
      <path d="M0 16 Q200 -8 401 16" fill="none" stroke="var(--brand)" stroke-width="2"/>
    </svg>
    <div class="banner">
      <div class="banner-title">Project Title goes here</div>
      <div class="banner-sub">Project Subtitle goes here</div>
    </div>
    <div class="banner-notch"></div>
    <h2 class="heading" style="top:257px">Lorem ipsum dolor sit amet</h2>
    <div class="cols" style="top:274px;height:270px">
      <div>
        <p>Lorem ipsum dolor sit amet, consectetur adipiscing elit, sed do eiusmod tempor incididunt ut labore et dolore magna aliqua. Ut enim ad minim veniam, quis nostrud exercitation ullamco laboris nisi ut aliquip ex ea commodo consequat. Duis aute irure dolor in reprehenderit in voluptate velit esse cillum dolore eu fugiat nulla pariatur. Excepteur sint occaecat cupidatat non proident, sunt in culpa qui officia deserunt mollit anim id est laborum."</p>
        <p>"Sed ut perspiciatis unde omnis iste natus error sit voluptatem accusantium doloremque laudantium, totam rem aperiam, eaque ipsa quae ab illo inventore veritatis et quasi architecto beatae vitae dicta sunt explicabo. Nemo enim ipsam voluptatem quia voluptas sit aspernatur aut odit aut fugit, sed quia consequuntur magni dolores eos qui ratione voluptatem sequi nesciunt. Neque porro quisquam est, qui</p>
      </div>
      <div>
        <p>"Lorem ipsum dolor sit amet, consectetur adipiscing elit, sed do eiusmod tempor incididunt ut labore et dolore magna aliqua. Ut enim ad minim veniam, quis nostrud exercitation ullamco laboris nisi ut aliquip ex ea commodo consequat. Duis aute irure dolor in reprehenderit in voluptate velit esse cillum dolore eu fugiat nulla pariatur. Excepteur sint occaecat cupidatat non proident, sunt in culpa qui officia deserunt mollit anim id est laborum."</p>
        <p>"Sed ut perspiciatis unde omnis iste natus error sit voluptatem accusantium doloremque laudantium, totam rem aperiam, eaque ipsa quae ab illo inventore veritatis et quasi architecto beatae vitae dicta sunt explicabo. Nemo enim ipsam voluptatem quia voluptas sit aspernatur aut odit aut fugit, sed quia consequuntur magni dolores eos qui ratione voluptatem sequi nesciunt. Neque porro</p>
      </div>
    </div>
    <div class="footer-rule"></div>
    <div class="folio">01</div>
  </section>

  <!-- Text page -->
  <section class="page page--text">
    <h1 class="page-title">Business Title here</h1>
    <div class="brand"><span class="brand-mark"></span>Brightway Advisory</div>
    <h2 class="heading" style="top:52px">Lorem ipsum dolor sit amet</h2>
    <div class="body" style="top:68px;height:92px">
      <p>Lorem ipsum dolor sit amet, consectetur adipiscing elit, sed do eiusmod tempor incididunt ut labore et dolore magna aliqua. Ut enim ad minim veniam, quis nostrud exercitation ullamco laboris nisi ut aliquip ex ea commodo consequat. Duis aute irure dolor in reprehenderit in voluptate velit esse cillum dolore eu fugiat nulla pariatur. Excepteur sint occaecat cupidatat non proident, sunt in culpa qui officia deserunt mollit anim id est laborum." Sed ut perspiciatis unde omnis iste natus error sit voluptatem accusantium doloremque laudantium, totam rem aperiam, eaque ipsa quae ab illo inventore veritatis et quasi architecto beatae vitae dicta sunt explicabo.</p>
    </div>
    <div class="body body--quote" style="top:170px;height:40px">
      <p>Ut enim ad minima veniam, quis nostrum exercitationem ullam corporis suscipit laboriosam, nisi ut aliquid ex ea commodi consequatur? Quis autem vel eum iure reprehenderit qui in ea voluptate velit esse quam nihil molestiae consequatur, vel illum qui dolorem eum fugiat quo voluptas nulla pariatur?"</p>
    </div>
    <h2 class="heading" style="top:233px">Lorem ipsum dolor sit amet</h2>
    <div class="cols" style="top:250px;height:280px">
      <div>
        <p>Lorem ipsum dolor sit amet, consectetur adipiscing elit, sed do eiusmod tempor incididunt ut labore et dolore magna aliqua. Ut enim ad minim veniam, quis nostrud exercitation ullamco laboris nisi ut aliquip ex ea commodo consequat. Duis aute irure dolor in reprehenderit in voluptate velit esse cillum dolore eu fugiat nulla pariatur. Excepteur sint occaecat cupidatat non proident, sunt in culpa qui officia deserunt mollit anim id est laborum."</p>
        <p>"Sed ut perspiciatis unde omnis iste natus error sit voluptatem accusantium doloremque laudantium, totam rem aperiam, eaque ipsa quae ab illo inventore veritatis et quasi architecto beatae vitae dicta sunt explicabo. Nemo enim ipsam voluptatem quia voluptas sit aspernatur aut odit aut fugit, sed quia consequuntur magni dolores eos qui ratione voluptatem sequi nesciunt. Neque porro quisquam est, qui dolorem ipsum quia dolor sit amet, consectetur, adipisci velit, sed quia non numquam eius modi</p>
      </div>
      <div>
        <p>"Lorem ipsum dolor sit amet, consectetur adipiscing elit, sed do eiusmod tempor incididunt ut labore et dolore magna aliqua. Ut enim ad minim veniam, quis nostrud exercitation ullamco laboris nisi ut aliquip ex ea commodo consequat. Duis aute irure dolor in reprehenderit in voluptate velit esse cillum dolore eu fugiat nulla pariatur. Excepteur sint occaecat cupidatat non proident, sunt in culpa qui officia deserunt mollit anim id est laborum."</p>
        <p>"Sed ut perspiciatis unde omnis iste natus error sit voluptatem accusantium doloremque laudantium, totam rem aperiam, eaque ipsa quae ab illo inventore veritatis et quasi architecto beatae vitae dicta sunt explicabo. Nemo enim ipsam voluptatem quia voluptas sit aspernatur aut odit aut fugit, sed quia consequuntur magni dolores eos qui ratione voluptatem sequi nesciunt. Neque porro quisquam est, qui dolorem ipsum quia dolor sit amet, consectetur, adipisci velit, sed quia non</p>
      </div>
    </div>
    <div class="footer-rule"></div>
    <div class="folio">01</div>
  </section>

  <!-- Tables page -->
  <section class="page page--tables">
    <h1 class="page-title">Business Title here</h1>
    <div class="brand"><span class="brand-mark"></span>Brightway Advisory</div>
    <h2 class="heading" style="top:52px">Lorem ipsum dolor sit amet</h2>
    <div class="body" style="top:68px;height:64px">
      <p>Lorem ipsum dolor sit amet, consectetur adipiscing elit, sed do eiusmod tempor incididunt ut labore et dolore magna aliqua. Ut enim ad minim veniam, quis nostrud exercitation ullamco laboris nisi ut aliquip ex ea commodo consequat. Duis aute irure dolor in reprehenderit in voluptate velit esse cillum dolore eu fugiat nulla pariatur. Excepteur sint occaecat cupidatat non proident, sunt in culpa qui officia deserunt mollit anim id est laborum.</p>
    </div>

    <h3 class="table-label" style="top:145px">Table Style 1</h3>
    <div class="table table--lined" style="top:164px">
      <div class="row row--head"><span>Title 1</span><span>Title 2</span><span>Title 3</span><span>Title 4</span><span>Title 5</span><span>Title 6</span></div>
      <div class="row row--body"><span>Lorem ipsum dolor</span><span>xxx</span><span>xxx</span><span>xxx</span><span>xxx</span><span>xxx</span></div>
      <div class="row row--body"><span>Lorem ipsum dolor</span><span>xxx</span><span>xxx</span><span>xxx</span><span>xxx</span><span>xxx</span></div>
      <div class="row row--body"><span>Lorem ipsum dolor</span><span>xxx</span><span>xxx</span><span>xxx</span><span>xxx</span><span>xxx</span></div>
      <div class="row row--body"><span>Lorem ipsum dolor</span><span>xxx</span><span>xxx</span><span>xxx</span><span>xxx</span><span>xxx</span></div>
    </div>

    <h3 class="table-label table-label--muted" style="top:270px">Table Style 2</h3>
    <div class="table table--shaded" style="top:286px">
      <div class="row row--head"><span>Title 1</span><span>Title 2</span><span>Title 3</span><span>Title 4</span><span>Title 5</span><span>Title 6</span></div>
      <div class="row row--body"><span>Lorem ipsum dolor</span><span>xxx</span><span>xxx</span><span>xxx</span><span>xxx</span><span>xxx</span></div>
      <div class="row row--body"><span>Lorem ipsum dolor</span><span>xxx</span><span>xxx</span><span>xxx</span><span>xxx</span><span>xxx</span></div>
      <div class="row row--body"><span>Lorem ipsum dolor</span><span>xxx</span><span>xxx</span><span>xxx</span><span>xxx</span><span>xxx</span></div>
      <div class="row row--body"><span>Lorem ipsum dolor</span><span>xxx</span><span>xxx</span><span>xxx</span><span>xxx</span><span>xxx</span></div>
    </div>

    <h3 class="table-label" style="top:388px">Table Style 3</h3>
    <div class="table table--boxed" style="top:408px">
      <div class="row row--head"><span>Title 1</span><span>Title 2</span><span>Title 3</span><span>Title 4</span><span>Title 5</span><span>Title 6</span></div>
      <div class="row row--body"><span>Lorem ipsum dolor</span><span>xxx</span><span>xxx</span><span>xxx</span><span>xxx</span><span>xxx</span></div>
      <div class="row row--body"><span>Lorem ipsum dolor</span><span>xxx</span><span>xxx</span><span>xxx</span><span>xxx</span><span>xxx</span></div>
      <div class="row row--body"><span>Lorem ipsum dolor</span><span>xxx</span><span>xxx</span><span>xxx</span><span>xxx</span><span>xxx</span></div>
      <div class="row row--body"><span>Lorem ipsum dolor</span><span>xxx</span><span>xxx</span><span>xxx</span><span>xxx</span><span>xxx</span></div>
    </div>
    <div class="footer-rule"></div>
    <div class="folio">01</div>
  </section>

  <!-- Charts page -->
  <section class="page page--charts">
    <h1 class="page-title">Business Title here</h1>
    <div class="brand"><span class="brand-mark"></span>Brightway Advisory</div>
    <h2 class="heading" style="top:52px">Lorem ipsum dolor sit amet</h2>
    <div class="body" style="top:68px;height:64px">
      <p>Lorem ipsum dolor sit amet, consectetur adipiscing elit, sed do eiusmod tempor incididunt ut labore et dolore magna aliqua. Ut enim ad minim veniam, quis nostrud exercitation ullamco laboris nisi ut aliquip ex ea commodo consequat. Duis aute irure dolor in reprehenderit in voluptate velit esse cillum dolore eu fugiat nulla pariatur. Excepteur sint occaecat cupidatat non proident, sunt in culpa qui officia deserunt mollit anim id est laborum.</p>
    </div>
    <h2 class="heading" style="top:145px">Graphs Title here</h2>
    <div class="body" style="top:160px;height:26px">
      <p>Lorem ipsum dolor sit amet, consectetur adipiscing elit, sed do eiusmod tempor incididunt ut labore et dolore magna aliqua. Ut enim ad minim veniam sed do eiusmod tempor</p>
    </div>
    <h2 class="heading" style="top:303px">PIE chart Title here</h2>
    <div class="body" style="top:318px;height:26px">
      <p>Lorem ipsum dolor sit amet, consectetur adipiscing elit, sed do eiusmod tempor incididunt ut labore et dolore magna aliqua. Ut enim ad minim veniam sed do eiusmod tempor</p>
    </div>

    <svg class="chart" viewBox="0 0 401 570" aria-label="Bar chart and line chart">
      <!-- bars -->
      <g>
        <rect x="42.4" y="238.4" width="26.4" height="49.6" fill="var(--brand)"/>
        <rect x="78.4" y="221.6" width="26.4" height="66.4" fill="var(--brand)"/>
        <rect x="113.6" y="246.4" width="26.4" height="41.6" fill="var(--brand)"/>
        <rect x="171.2" y="249.6" width="22.4" height="38.4" fill="var(--brand-light)"/>
        <rect x="198.4" y="221.6" width="22.4" height="66.4" fill="var(--brand-light)"/>
        <rect x="225.6" y="270.4" width="22.4" height="17.6" fill="var(--brand-light)"/>
        <rect x="276" y="235.2" width="22.4" height="52.8" fill="var(--grey)"/>
        <rect x="304" y="202.4" width="21.6" height="85.6" fill="var(--grey)"/>
        <rect x="329.6" y="276.8" width="22.4" height="11.2" fill="var(--grey)"/>
      </g>
      <!-- line chart grid -->
      <g stroke="#ddd" stroke-width="0.6">
        <line x1="82" y1="484.6" x2="324" y2="484.6"/>
        <line x1="82" y1="463.6" x2="324" y2="463.6"/>
        <line x1="82" y1="442.6" x2="324" y2="442.6"/>
        <line x1="82" y1="421.6" x2="324" y2="421.6"/>
        <line x1="82" y1="400.6" x2="324" y2="400.6"/>
        <line x1="82" y1="379.6" x2="324" y2="379.6"/>
        <line x1="82" y1="364" x2="324" y2="364"/>
        <line x1="102.2" y1="364" x2="102.2" y2="505.6"/>
        <line x1="122.4" y1="364" x2="122.4" y2="505.6"/>
        <line x1="142.6" y1="364" x2="142.6" y2="505.6"/>
        <line x1="162.8" y1="364" x2="162.8" y2="505.6"/>
        <line x1="183" y1="364" x2="183" y2="505.6"/>
        <line x1="203.2" y1="364" x2="203.2" y2="505.6"/>
        <line x1="223.4" y1="364" x2="223.4" y2="505.6"/>
        <line x1="243.6" y1="364" x2="243.6" y2="505.6"/>
        <line x1="263.8" y1="364" x2="263.8" y2="505.6"/>
        <line x1="284" y1="364" x2="284" y2="505.6"/>
        <line x1="304.2" y1="364" x2="304.2" y2="505.6"/>
        <line x1="324" y1="364" x2="324" y2="505.6"/>
      </g>
      <g stroke="#aaa" stroke-width="1.2">
        <line x1="82" y1="364" x2="82" y2="505.6"/>
        <line x1="82" y1="505.6" x2="324" y2="505.6"/>
      </g>
      <g font-family="Open Sans, sans-serif" font-size="5" fill="#aaa" text-anchor="middle">
        <text x="76" y="507">0</text><text x="76" y="486">1</text><text x="76" y="465">2</text>
        <text x="76" y="444">3</text><text x="76" y="423">4</text><text x="76" y="402">5</text><text x="76" y="381">6</text>
        <text x="102.2" y="514">1</text><text x="122.4" y="514">2</text><text x="142.6" y="514">3</text>
        <text x="162.8" y="514">4</text><text x="183" y="514">5</text><text x="203.2" y="514">6</text>
        <text x="223.4" y="514">7</text><text x="243.6" y="514">8</text><text x="263.8" y="514">9</text>
        <text x="284" y="514">10</text><text x="304.2" y="514">11</text>
      </g>
      <g fill="none" stroke-width="1.4">
        <path d="M82 505.6 C105 480 120 445 142.6 463.6 C170 455 195 495 223.4 476.2 C250 470 280 400 304.2 379.6" stroke="var(--brand-light)"/>
        <path d="M82 505.6 C100 470 115 445 142.6 442.6 C175 420 200 425 223.4 442.6 C245 460 265 485 284 468 C292 462 298 460 304.2 463.6" stroke="#999"/>
        <path d="M82 505.6 C100 465 115 435 142.6 430 C170 418 200 405 223.4 421.6 C250 432 270 400 304.2 400.6" stroke="var(--brand-mid)"/>
        <path d="M82 505.6 C100 455 115 425 142.6 421.6 C170 405 200 395 223.4 400.6 C250 410 285 405 304.2 390.1" stroke="#1f65c0"/>
        <path d="M82 505.6 C100 450 115 410 142.6 400.6 C175 395 195 380 223.4 383.8 C260 388 285 410 304.2 432.1" stroke="var(--brand)"/>
      </g>
      <g>
        <circle cx="82" cy="505.6" r="3" fill="var(--brand)"/>
        <circle cx="142.6" cy="463.6" r="2.6" fill="var(--brand-light)"/>
        <circle cx="223.4" cy="476.2" r="2.6" fill="var(--brand-light)"/>
        <circle cx="304.2" cy="379.6" r="2.6" fill="var(--brand-light)"/>
        <circle cx="142.6" cy="442.6" r="2.6" fill="#999"/>
        <circle cx="223.4" cy="442.6" r="2.6" fill="#999"/>
        <circle cx="304.2" cy="463.6" r="2.6" fill="#999"/>
        <circle cx="142.6" cy="430" r="2.6" fill="var(--brand-mid)"/>
        <circle cx="223.4" cy="421.6" r="2.6" fill="var(--brand-mid)"/>
        <circle cx="304.2" cy="400.6" r="2.6" fill="var(--brand-mid)"/>
        <circle cx="142.6" cy="421.6" r="2.6" fill="#1f65c0"/>
        <circle cx="223.4" cy="400.6" r="2.6" fill="#1f65c0"/>
        <circle cx="304.2" cy="390.1" r="2.6" fill="#1f65c0"/>
        <circle cx="142.6" cy="400.6" r="2.6" fill="var(--brand)"/>
        <circle cx="223.4" cy="383.8" r="2.6" fill="var(--brand)"/>
        <circle cx="304.2" cy="432.1" r="2.6" fill="var(--brand)"/>
      </g>
    </svg>
    <div class="footer-rule"></div>
    <div class="folio">01</div>
  </section>

</main>
</body>
</html>
```